Digital Transformation Company Trade Show Banners

I am looking for help designing banners for an upcoming trade show. One would be for our company and one would be for our product. I am planning on purchasing retractable banners with a size of 33" x 81". Details are attached.

```html
<!DOCTYPE html>
<html lang="en">
<head>
<meta charset="utf-8">
<title>Veltrion Technology – Roll-up Banner</title>
<link rel="stylesheet" href="https://fonts.googleapis.com/css2?family=Exo+2:wght@600;700&family=Saira+Semi+Condensed:wght@600&display=swap">
<style>
  :root {
    --navy: #0f2b47;
    --navy-deep: #0a2038;
    --orange: #e8681e;
    --white: #ffffff;
    --stage: #e4e5e1;
    --warm: #7a5438;
    --warm-light: #b88a5c;
  }
  html, body {
    margin: 0;
    width: 1200px;
    height: 1200px;
    overflow: hidden;
    background: var(--stage);
  }
  .canvas {
    position: relative;
    width: 1200px;
    height: 1200px;
  }
  .banner {
    position: absolute;
    left: 364px;
    top: 20px;
    width: 473px;
    height: 1160px;
    box-shadow: 0 6px 24px rgba(0,0,0,0.18);
  }
  .headline {
    font-family: "Exo 2", sans-serif;
    font-weight: 700;
    font-size: 25px;
    letter-spacing: 0.5px;
    fill: var(--white);
  }
  .service-label {
    font-family: "Saira Semi Condensed", sans-serif;
    font-weight: 600;
    font-size: 18px;
    fill: var(--navy);
  }
  .brand-name, .brand-sub {
    font-family: "Exo 2", sans-serif;
    font-weight: 700;
    fill: var(--navy);
  }
  .brand-name { font-size: 38px; letter-spacing: 1px; }
  .brand-sub { font-size: 10px; letter-spacing: 5px; }
  .web-address {
    font-family: "Exo 2", sans-serif;
    font-weight: 700;
    font-size: 20px;
    letter-spacing: 2px;
    fill: var(--navy);
  }
  .icon-line { fill: none; stroke: var(--white); stroke-width: 2.2; stroke-linejoin: round; stroke-linecap: round; }
  .icon-fill { fill: var(--white); }
</style>
</head>
<body>
<div class="canvas">
  <svg class="banner" viewBox="0 0 330 810" xmlns="http://www.w3.org/2000/svg">
    <defs>
      <linearGradient id="photoTone" x1="0" y1="0" x2="1" y2="0.6">
        <stop offset="0" stop-color="var(--navy-deep)"/>
        <stop offset="0.4" stop-color="#1c3550"/>
        <stop offset="0.75" stop-color="var(--warm)"/>
        <stop offset="1" stop-color="var(--warm-light)"/>
      </linearGradient>
      <linearGradient id="topShade" x1="0" y1="0" x2="0" y2="1">
        <stop offset="0" stop-color="var(--navy)" stop-opacity="1"/>
        <stop offset="0.45" stop-color="var(--navy)" stop-opacity="0.6"/>
        <stop offset="1" stop-color="var(--navy)" stop-opacity="0"/>
      </linearGradient>
      <radialGradient id="networkTone" cx="0.6" cy="0.4" r="0.7">
        <stop offset="0" stop-color="#eceef1"/>
        <stop offset="1" stop-color="#ffffff"/>
      </radialGradient>
    </defs>

    <!-- base -->
    <rect class="banner-base" width="330" height="810" fill="var(--white)"/>
    <rect class="network-backdrop" x="0" y="330" width="330" height="430" fill="url(#networkTone)" role="img" aria-label="Faint network of connected dots and lines"/>

    <!-- photo area -->
    <g class="hero-photo" role="img" aria-label="Photo of two smiling colleagues talking in a modern office">
      <polygon points="0,0 330,0 330,420 105,352 0,312" fill="url(#photoTone)"/>
      <polygon points="0,0 330,0 330,260 0,260" fill="url(#topShade)"/>
    </g>

    <!-- corner accent -->
    <polygon class="corner-white" points="168,0 330,0 330,82" fill="var(--white)"/>
    <polygon class="corner-orange" points="212,0 322,0 322,58" fill="var(--orange)"/>

    <!-- headline -->
    <text class="headline" x="22" y="80">LEARN TO</text>
    <text class="headline" x="22" y="110">ACHIEVE YOUR</text>
    <text class="headline" x="22" y="140">DIGITAL GOALS</text>
    <rect class="headline-rule" x="23" y="152" width="86" height="3" fill="var(--orange)"/>

    <!-- orange band -->
    <polygon class="accent-band" points="0,283 105,324 105,368 0,326" fill="var(--orange)"/>

    <!-- services -->
    <g class="service-list">
      <path class="service-arc" d="M93,410 A41,41 0 0 1 93,492" fill="none" stroke="var(--orange)" stroke-width="9"/>
      <path class="service-arc" d="M93,488 A41,41 0 0 0 93,570" fill="none" stroke="var(--orange)" stroke-width="9"/>
      <path class="service-arc" d="M93,566 A41,41 0 0 1 93,648" fill="none" stroke="var(--orange)" stroke-width="9"/>

      <!-- digital transformation -->
      <circle cx="93" cy="451" r="37" fill="var(--navy)"/>
      <g class="icon-gear" transform="translate(93 451)">
        <circle r="12" fill="none" stroke="var(--white)" stroke-width="5" stroke-dasharray="4.2 3.3"/>
        <circle r="9" class="icon-fill"/>
        <circle r="4" fill="var(--navy)"/>
        <rect x="8" y="-9" width="3" height="3" class="icon-fill"/>
        <rect x="13" y="-4" width="3" height="3" class="icon-fill"/>
        <rect x="10" y="3" width="3" height="3" class="icon-fill"/>
        <rect x="16" y="8" width="3" height="3" class="icon-fill"/>
      </g>
      <text class="service-label" x="152" y="444">Digital</text>
      <text class="service-label" x="152" y="466">Transformation</text>

      <!-- cybersecurity -->
      <circle cx="93" cy="529" r="37" fill="var(--navy)"/>
      <g class="icon-shield" transform="translate(93 529)">
        <path class="icon-line" d="M0,-18 L15,-12 C15,4 9,13 0,18 C-9,13 -15,4 -15,-12 Z"/>
        <rect x="-5" y="-2" width="10" height="8" rx="1" class="icon-fill"/>
        <path class="icon-line" d="M-3,-2 V-5 A3,3 0 0 1 3,-5 V-2" stroke-width="1.8"/>
      </g>
      <text class="service-label" x="152" y="535">Cybersecurity</text>

      <!-- software development -->
      <circle cx="93" cy="607" r="37" fill="var(--navy)"/>
      <g class="icon-monitor" transform="translate(93 607)">
        <rect class="icon-line" x="-16" y="-13" width="32" height="22" rx="1.5"/>
        <path class="icon-line" d="M-5,14 H5 M0,9 V14"/>
        <path class="icon-line" d="M-12,-8 H-2 M-12,-4 H-6" stroke-width="1.6"/>
        <path class="icon-line" d="M3,-3 L0,1 L3,5 M9,-3 L12,1 L9,5" stroke-width="1.8"/>
      </g>
      <text class="service-label" x="152" y="601">Software</text>
      <text class="service-label" x="152" y="623">Development</text>
    </g>

    <!-- brand -->
    <g class="brand">
      <rect class="brand-mark" x="38" y="694" width="16" height="16" fill="var(--orange)"/>
      <text class="brand-name" x="62" y="712">VELTRION</text>
      <text class="brand-sub" x="64" y="728">TECHNOLOGY</text>
    </g>
    <text class="web-address" x="165" y="772" text-anchor="middle">www.veltrion.io</text>
  </svg>
</div>
</body>
</html>
```